Stationery including letterhead, business cards, for a new Chartered Accounting Practice

I need a new set of stationery including letterhead, business cards, for a new Chartered Accounting Practice based in Melbourne, Victoria, Australia called "Brint Holloway, Chartered Accountant".

I will be providing Auditing and general consulting advice to small and medium business enterprises. The final design should communicate trust, wisdom and security.

Target Market(s)

Target Market English speaking, Australians. Proprietors small and medium sized businesses - aged 45-65. Fellow professionals - lawyers, investment consultants, other accountants. Retirees - aged 60 and over

Industry/Entity Type

Accountant

Font styles to use
Serif

Colors
0355a3

Requirements
Must have
• The final design should convey trust, wisdom and security.
• Names of practice "Brint Holloway , Chartered Accountant"
• Contact details:
• Address 284 Marbury Street, Tallow Creek, Victoria, 3172, Australia
• Telephone: 047 000 3158
• Email: brintholloway@postquill.example
Nice to have
• an expensive and professional design, the letterhead should be timeless with a logo on white space
Should not have
• no bright/fluro colours

```html
<!DOCTYPE html>
<html lang="en">
<head>
<meta charset="utf-8">
<title>Brint Holloway, Chartered Accountant — Stationery</title>
<link rel="stylesheet" href="https://fonts.googleapis.com/css2?family=PT+Sans&family=Arimo&display=swap">
<style>
  :root {
    --backdrop: #c8c8c8;
    --ink: #1e1e1e;
    --ink-soft: #2c2c2c;
    --paper: #f4f4f4;
    --card-dark: #1a1a1a;
    --mark-light: #f2f2f2;
  }
  * { margin: 0; padding: 0; box-sizing: border-box; }
  html, body { width: 1200px; height: 811px; overflow: hidden; }
  body {
    background: var(--backdrop);
    position: relative;
    font-family: "PT Sans", sans-serif;
    color: var(--ink);
  }
  .brand-lockup {
    position: absolute;
    left: 0; top: 124px; width: 1200px;
    text-align: center;
  }
  .brand-square {
    display: block;
    width: 56px; height: 58px;
    margin: 0 auto 18px;
    border: 4px solid var(--ink);
  }
  .brand-name {
    font-size: 29px;
    letter-spacing: 0.5px;
    line-height: 1;
    text-transform: uppercase;
  }
  .brand-title {
    font-size: 14px;
    color: var(--ink-soft);
    margin-top: 4px;
  }
  .card {
    position: absolute;
    top: 409px;
    width: 484px; height: 271px;
  }
  .card-front { left: 94px; background: var(--paper); }
  .card-back { left: 624px; background: var(--card-dark); }
  .card-square {
    position: absolute;
    left: 38px; top: 45px;
    width: 48px; height: 50px;
    border: 4px solid var(--ink);
  }
  .card-name {
    position: absolute;
    left: 98px; top: 52px;
    font-size: 24px;
    line-height: 1;
    text-transform: uppercase;
    letter-spacing: 0.3px;
  }
  .card-title {
    position: absolute;
    left: 98px; top: 80px;
    font-size: 12px;
    color: var(--ink-soft);
  }
  .card-contact {
    position: absolute;
    left: 38px; top: 214px;
    font-family: "Arimo", sans-serif;
    font-size: 11px;
    line-height: 14px;
    color: var(--ink);
  }
  .card-back .back-square {
    position: absolute;
    left: 209px; top: 104px;
    width: 66px; height: 66px;
    border: 4px solid var(--mark-light);
  }
</style>
</head>
<body>
  <header class="brand-lockup">
    <span class="brand-square" aria-hidden="true"></span>
    <div class="brand-name">Brint Holloway</div>
    <div class="brand-title">Chartered Accountant</div>
  </header>

  <section class="card card-front" aria-label="Business card front">
    <span class="card-square" aria-hidden="true"></span>
    <div class="card-name">Brint Holloway</div>
    <div class="card-title">Chartered Accountant</div>
    <div class="card-contact">
      047 000 3158 / brintholloway@postquill.example<br>
      284 Marbury Street, Tallow Creek, Victoria, 3172, Australia
    </div>
  </section>

  <section class="card card-back" aria-label="Business card back">
    <span class="back-square" aria-hidden="true"></span>
  </section>
</body>
</html>
```